Nourish Kin Network Australia needs a flyer to update to new style guide and modernise

Nourish Kin Network Australia (NKNA) is looking to update their flyers. NKNA is a volunteer, parent-led, not for profit organisation that supports and advocates for parents and carers of someone with an eating disorder. Attached is some flyers and brochures that we are currently working with, since producing those we have introduced a style guide, also attached. The flyer needs to be visually appealing and professional.We are hoping to combine the NKNA flyer and NKNA Brochure into a single item. We also need to add in our new Uplift support groups.This would replace the back page of the brochure ("NKNA Will endeavour to facilitate and advocate...) Please refer to last pages of style guide for Uplift details.If the document could be produced to allow changes to wording as certain details will need to be refined or edited in the future.

Target Market(s)

Parents and Carers of someone with a life threatening mental illness

Font styles to use
Other font styles liked:
• Avenir Next

Colors

Designer to choose colors to be used in the design.

Requirements
Must have
• NKNA logos and font matching style guide
Nice to have
• Clean and professional looking design, visually appealing
• Easy to read
Should not have
• Upsetting images

```html
<!DOCTYPE html>
<html lang="en">
<head>
<meta charset="utf-8">
<title>Nourish Kin Network Australia – Flyer</title>
<link href="https://fonts.googleapis.com/css2?family=Montserrat:wght@500;600;700;800&family=Nunito+Sans:wght@400;600;700;800;900&display=swap" rel="stylesheet">
<style>
  :root {
    --purple: #8a2b86;
    --purple-dark: #6e1f6b;
    --green: #7ab648;
    --green-dark: #5f9a33;
    --ink: #3d3d3f;
    --grey-soft: #eeeeef;
    --white: #ffffff;
    --photo-warm: #c9a58a;
    --photo-cool: #7f94a8;
  }
  * { margin: 0; padding: 0; box-sizing: border-box; }
  html, body { width: 720px; height: 1200px; overflow: hidden; background: var(--white); }
  .flyer {
    position: relative; width: 720px; height: 1200px; overflow: hidden;
    background: var(--white);
    font-family: "Nunito Sans", "Helvetica Neue", Arial, sans-serif;
    color: var(--ink);
  }
  .flyer-shapes { position: absolute; inset: 0; }
  .brand {
    position: absolute; left: 34px; top: 34px; width: 260px;
    display: flex; align-items: center; gap: 12px;
    color: var(--purple);
  }
  .brand-dot { width: 46px; height: 46px; border-radius: 50%; background: var(--purple); flex: none; }
  .brand-text { font-weight: 800; }
  .brand-acronym { font-size: 30px; line-height: 1; letter-spacing: 1px; }
  .brand-name { font-size: 13px; line-height: 1.25; margin-top: 4px; }

  .headline {
    position: absolute; left: 38px; top: 612px; width: 345px;
    font-family: "Nunito Sans", "Helvetica Neue", Arial, sans-serif;
    white-space: nowrap;
  }
  .headline-lead {
    display: block; font-size: 21px; line-height: 28px;
    font-weight: 600; color: var(--ink); letter-spacing: 0.2px;
  }
  .headline-key {
    display: block; font-size: 33px; line-height: 38px;
    font-weight: 900; color: var(--purple); margin-top: 2px;
  }

  .concerns {
    position: absolute; left: 40px; top: 712px; width: 325px;
    list-style: none;
  }
  .concerns li {
    position: relative; padding-left: 28px; margin-bottom: 22px;
    font-size: 18px; line-height: 1.4; color: var(--ink);
  }
  .concerns li::before {
    content: ""; position: absolute; left: 0; top: 8px;
    width: 12px; height: 12px; border-radius: 50%; background: var(--purple);
  }

  .support-points {
    position: absolute; left: 400px; top: 560px; width: 300px;
    list-style: none; color: var(--white);
  }
  .support-points li {
    font-size: 18px; font-weight: 800; line-height: 1.3;
    padding: 16px 0; border-bottom: 2px solid rgba(255,255,255,0.55);
  }
  .support-points li:last-child { border-bottom: none; }

  .footer-bar {
    position: absolute; left: 0; bottom: 0; width: 720px; height: 104px;
    background: var(--green);
    display: flex; align-items: center; justify-content: space-between;
    padding: 0 40px; color: var(--white);
  }
  .footer-web { display: flex; align-items: center; gap: 14px; font-size: 26px; font-weight: 700; }
  .footer-call { text-align: right; font-size: 17px; font-weight: 700; line-height: 1.35; }
</style>
</head>
<body>
<main class="flyer">
  <svg class="flyer-shapes" width="720" height="1200" viewBox="0 0 720 1200">
    <defs>
      <linearGradient id="photoFamily" x1="0" y1="0" x2="1" y2="1">
        <stop offset="0" stop-color="#7f94a8"/>
        <stop offset="1" stop-color="#c9a58a"/>
      </linearGradient>
      <linearGradient id="photoCarers" x1="0" y1="0" x2="1" y2="1">
        <stop offset="0" stop-color="#b8c3cc"/>
        <stop offset="1" stop-color="#a88b72"/>
      </linearGradient>
    </defs>
    <path class="swoosh" d="M0 300 C 160 380, 260 560, 380 640 L 380 660 C 240 600, 140 420, 0 340 Z" fill="var(--grey-soft)"/>
    <path class="swoosh" d="M0 1010 C 120 970, 260 990, 385 1050 L 385 1096 L 0 1096 Z" fill="var(--grey-soft)"/>
    <polygon class="support-panel" points="385,500 720,420 720,1096 385,1096" fill="var(--purple)"/>
    <circle cx="545" cy="215" r="198" fill="var(--white)"/>
    <path class="photo-ring" d="M 372 150 A 186 186 0 0 0 520 400" fill="none" stroke="var(--purple)" stroke-width="14"/>
    <circle cx="548" cy="215" r="180" fill="url(#photoFamily)" role="img" aria-label="Photo: smiling grandfather and young man embracing"/>
    <circle cx="160" cy="470" r="112" fill="var(--white)"/>
    <path class="photo-ring" d="M 52 455 A 108 108 0 0 0 260 515" fill="none" stroke="var(--purple)" stroke-width="10"/>
    <circle cx="160" cy="470" r="100" fill="url(#photoCarers)" role="img" aria-label="Photo: parents sitting together looking at a tablet"/>
  </svg>

  <header class="brand">
    <span class="brand-dot"></span>
    <div class="brand-text">
      <div class="brand-acronym">NKNA</div>
      <div class="brand-name">Nourish Kin Network Australia</div>
    </div>
  </header>

  <h1 class="headline">
    <span class="headline-lead">DOES YOUR CHILD HAVE AN</span>
    <span class="headline-key">EATING DISORDER?</span>
  </h1>

  <ul class="concerns">
    <li>Are you concerned your child has a problem with eating, weight or body image?</li>
    <li>Parents and carers play a pivotal role in treatment &amp; recovery of eating disorders.</li>
    <li>NKNA will help you get the skills &amp; knowledge you need to support your loved one through this illness</li>
  </ul>

  <ul class="support-points">
    <li>NKNA supports families and carers of people with an eating disorder</li>
    <li>Early action is imperative</li>
    <li>NKNA will help guide you to appropriate resources &amp; support</li>
    <li>NKNA will help guide you to appropriate resources &amp; support</li>
    <li>NKNA acknowledges the importance of well-being of ALL family members throughout the ED journey</li>
  </ul>

  <footer class="footer-bar">
    <div class="footer-web">
      <svg width="34" height="34" viewBox="0 0 34 34" aria-hidden="true">
        <g fill="none" stroke="var(--white)" stroke-width="2.2">
          <circle cx="17" cy="17" r="14"/>
          <ellipse cx="17" cy="17" rx="6" ry="14"/>
          <line x1="3" y1="17" x2="31" y2="17"/>
          <path d="M6 9 H28 M6 25 H28"/>
        </g>
      </svg>
      <span>www.nkna.org.au</span>
    </div>
    <div class="footer-call">Please join us today!<br>Donations welcome</div>
  </footer>
</main>
</body>
</html>
```